Business Card Design

We are starting up a new Family run Business mainly offering a Free House Clearance service. We also offer the following chargeable services which include a Removals Service, Delivery and Collection of Items sold or purchased on Bidloft, Swapcorner etc, including Motorcycles, Piano's, Furniture, Electrical appliances.
As there are a few Companies offering similar services we need to stand out and show what we do at a glance while appearing Professional and approachable
Updates

TidyNests

i  am liking some of the colours and designs so far but would like to see a few of our services listed as 1 or 2 have already done if this is possible and maybe some emphasis on the FREE House Clearance. thank you 
best regards
derek

Target Market(s)

Commercial and Domestic Tenants and Landlords aswell as Families looking for a friendly sympathetic clearance service after bereavement

Industry/Entity Type

Business

Contact Information for Business Card

TidyNests,
HouseClearance and Removals,
Brynmor Vale
CF47 2RL
Tel: 07831562904
Email: enquiries@tidynests.example

```html
<!DOCTYPE html>
<html lang="en">
<head>
<meta charset="utf-8">
<title>Tidy Nests – Business Card</title>
<link rel="stylesheet" href="https://fonts.googleapis.com/css2?family=Poppins:wght@500;600;700&display=swap">
<style>
  :root {
    --backdrop: #e9e6e1;
    --card: #f7f7f5;
    --green: #2f9a4c;
    --green-text: #1f9a45;
    --teal: #3a9a92;
    --blue: #33609c;
    --white: #ffffff;
    --shadow: rgba(40, 30, 20, 0.25);
  }
  * { margin: 0; padding: 0; box-sizing: border-box; }
  html, body {
    width: 1200px; height: 723px; overflow: hidden;
    background: var(--backdrop);
    font-family: "Poppins", sans-serif;
  }
  .stage {
    width: 1200px; height: 723px;
    display: flex; align-items: center; justify-content: center; gap: 80px;
  }
  .card {
    position: relative;
    width: 340px; height: 510px;
    background: var(--card);
    box-shadow: 0 10px 28px var(--shadow);
    overflow: hidden;
  }
  .card__bands { position: absolute; inset: 0; width: 100%; height: 100%; }
  .band--blue { fill: var(--blue); }
  .band--teal { fill: var(--teal); }
  .band--green { fill: var(--green); }

  /* Front */
  .brand { position: absolute; left: 30px; right: 20px; bottom: 40px; }
  .brand__name {
    color: var(--green-text); font-weight: 700;
    font-size: 46px; line-height: 1; letter-spacing: -0.5px;
  }
  .brand__tagline {
    color: var(--teal); font-weight: 600;
    font-size: 16px; line-height: 1.2; margin-top: 8px;
  }
  .brand__offer {
    display: flex; align-items: center; gap: 8px;
    margin-top: 14px;
    color: var(--blue); font-weight: 700; font-size: 16px; line-height: 1;
  }
  .brand__free {
    background: var(--green); color: var(--white);
    font-weight: 700; font-size: 16px; line-height: 1;
    padding: 6px 10px; border-radius: 4px; letter-spacing: 1px;
  }

  /* Back */
  .services { position: absolute; left: 30px; right: 20px; top: 272px; }
  .services__title {
    color: var(--blue); font-weight: 700; font-size: 14px; line-height: 1;
    text-transform: uppercase; letter-spacing: 1px;
  }
  .services__list {
    list-style: none; margin-top: 8px;
    display: flex; flex-wrap: wrap; gap: 4px 12px;
  }
  .services__item {
    color: var(--teal); font-weight: 600; font-size: 12px; line-height: 1.3;
    display: flex; align-items: center; gap: 5px;
  }
  .services__item::before {
    content: ""; width: 5px; height: 5px; border-radius: 50%; background: var(--green);
  }

  .contact { position: absolute; left: 30px; right: 16px; bottom: 36px; list-style: none; }
  .contact__item {
    display: flex; align-items: center; gap: 8px;
    color: var(--green-text); font-weight: 700;
    font-size: 16px; line-height: 1; margin-top: 14px;
    white-space: nowrap;
  }
  .contact__icon { width: 14px; height: 14px; flex: none; }
  .contact__icon path, .contact__icon rect { fill: none; stroke: var(--green-text); stroke-width: 1.8; stroke-linejoin: round; }
</style>
</head>
<body>
<main class="stage">

  <section class="card card--front">
    <svg class="card__bands" viewBox="0 0 340 510" aria-hidden="true">
      <circle class="band--blue" cx="210" cy="-160" r="460"/>
      <circle class="band--teal" cx="210" cy="-160" r="385"/>
      <circle class="band--green" cx="210" cy="-160" r="315"/>
    </svg>
    <div class="brand">
      <div class="brand__name">Tidy Nests</div>
      <div class="brand__tagline">House Clearance and Removals</div>
      <div class="brand__offer"><span class="brand__free">FREE</span>House Clearance</div>
    </div>
  </section>

  <section class="card card--back">
    <svg class="card__bands" viewBox="0 0 340 510" aria-hidden="true">
      <circle class="band--blue" cx="210" cy="-160" r="410"/>
      <circle class="band--teal" cx="210" cy="-160" r="340"/>
      <circle class="band--green" cx="210" cy="-160" r="275"/>
    </svg>
    <div class="services">
      <div class="services__title">Our Services</div>
      <ul class="services__list">
        <li class="services__item">Removals</li>
        <li class="services__item">Bidloft &amp; Swapcorner Deliveries</li>
        <li class="services__item">Motorcycles</li>
        <li class="services__item">Pianos</li>
        <li class="services__item">Furniture</li>
        <li class="services__item">Electrical Appliances</li>
      </ul>
    </div>
    <ul class="contact">
      <li class="contact__item">
        <svg class="contact__icon" viewBox="0 0 14 14" aria-hidden="true"><path d="M7 13 C3 8 2.5 6.5 2.5 5 a4.5 4.5 0 0 1 9 0 c0 1.5-.5 3-4.5 8z"/><path d="M7 3.8 a1.2 1.2 0 1 1 0 2.4 a1.2 1.2 0 1 1 0-2.4z"/></svg>
        Brynmor Vale CF47 2RL
      </li>
      <li class="contact__item">
        <svg class="contact__icon" viewBox="0 0 14 14" aria-hidden="true"><path d="M3 1.5 l2.2 2.6 -1.2 1.6 c.8 1.8 2.2 3.2 4 4 l1.6-1.2 2.6 2.2 -1.3 1.8 C6 12.3 1.7 8 1.2 2.8z"/></svg>
        07831562904
      </li>
      <li class="contact__item">
        <svg class="contact__icon" viewBox="0 0 14 14" aria-hidden="true"><rect x="1" y="3" width="12" height="8.5"/><path d="M1 3 l6 5 6-5"/></svg>
        enquiries@tidynests.example
      </li>
    </ul>
  </section>

</main>
</body>
</html>
```